Author book launch promotion design for social media

We are organising an authors book launch event and require an author promotion design that will be used on social media (Chatterbook, netted) promotion.

The design must have the author's photo, image of their book, the event logo, details of the event plus website address (penfairhall.com.au).

Details of the event can be found at penfairhall.com.au.

the design has to be attractive and inviting and colours in accordance with the brand colours.

You can choose 1 one of the book images attached
Author name: Dr Tarek Bismil
Event Details
LAUNCH YOUR BOOK IN STYLE

Quillmark Reading Fair and Showcase 2022
7 - 8 October 2022
Melbourne Larkvale Centre
14 Corrigal St, Southbank Melbourne

For registration and ticketing visit:
penfairhall.com.au

I have attached also a sample promo. Please be creative.

```html
<!DOCTYPE html>
<html lang="en">
<head>
<meta charset="utf-8">
<title>Book Launch Event – Dr Tarek Bismil</title>
<link href="https://fonts.googleapis.com/css2?family=Archivo+Black&family=Anton&family=Playfair+Display:wght@400&family=Great+Vibes&family=Lexend:wght@400;500;600;700&display=swap" rel="stylesheet">
<style>
  :root {
    --navy-deep: #0f2d42;
    --navy-ink: #123048;
    --band-blue: #336693;
    --ring-blue: #35689a;
    --text-blue: #2f5a88;
    --rose: #c9415a;
    --rose-dark: #a9334b;
    --cover-rose: #d3295a;
    --gold: #e0a43a;
    --white: #ffffff;
    --ink: #222428;
  }
  * { margin: 0; padding: 0; box-sizing: border-box; }
  html, body { width: 1200px; height: 873px; overflow: hidden; background: var(--navy-deep); }
  .canvas { position: relative; width: 1200px; height: 873px; background: var(--navy-deep); }
  .panel {
    position: absolute; left: 163px; top: 43px; width: 873px; height: 786px;
    background: radial-gradient(ellipse at 45% 40%, #ffffff 0%, #f3f3f4 45%, #d9d9db 100%);
    overflow: hidden;
  }

  /* Headline */
  .headline { position: absolute; left: 0; top: 0; width: 530px; font-weight: 400; }
  .headline__big {
    position: absolute; font-family: "Archivo Black", sans-serif; color: var(--rose);
    background: linear-gradient(90deg, var(--rose-dark), var(--rose) 50%, var(--rose-dark));
    -webkit-background-clip: text; background-clip: text; -webkit-text-fill-color: transparent;
    filter: drop-shadow(2px 3px 3px rgba(0,0,0,.25));
    line-height: 1; white-space: nowrap;
  }
  .headline__book { left: 118px; top: 47px; font-size: 91px; letter-spacing: 1px; }
  .headline__launch { left: 56px; top: 130px; font-size: 91px; letter-spacing: -1px; }
  .headline__event {
    position: absolute; left: 162px; top: 222px; font-family: "Playfair Display", serif; font-weight: 400;
    font-size: 68px; color: var(--navy-ink); line-height: 1; letter-spacing: 1px;
    text-shadow: 2px 3px 3px rgba(0,0,0,.2);
  }

  /* Author */
  .author-photo {
    position: absolute; left: 529px; top: 39px; width: 306px; height: 306px; border-radius: 50%;
    border: 8px solid var(--ring-blue);
    background: radial-gradient(circle at 50% 40%, #6b5a52 0%, #3a3a3c 45%, #1c1c1e 100%);
  }
  .author-name { font-family: "Great Vibes", cursive; color: var(--gold); font-size: 58px; line-height: 1; }
  .author-name__line {
    position: absolute; white-space: nowrap;
    text-shadow: 1px 2px 2px rgba(0,0,0,.25);
  }
  .author-name__first { left: 607px; top: 274px; }
  .author-name__last { left: 662px; top: 330px; }

  /* Date band */
  .date-band { position: absolute; left: 0; top: 419px; width: 873px; height: 181px; background: var(--band-blue); }

  /* Book */
  .book {
    position: absolute; left: 109px; top: 325px; width: 249px; height: 392px;
    transform: skewY(-3deg); transform-origin: left top;
    box-shadow: 6px 10px 16px rgba(0,0,0,.3);
    display: flex;
  }
  .book__spine {
    width: 20px; height: 100%;
    background: linear-gradient(90deg, #b01f49, var(--cover-rose) 60%, #a81d45);
    display: flex; flex-direction: column; align-items: center; justify-content: space-between;
    padding: 22px 0 30px;
  }
  .book__spine-text {
    writing-mode: vertical-rl; font-family: "Lexend", sans-serif; font-size: 6px; font-weight: 700;
    letter-spacing: 1.2px; color: var(--white); white-space: nowrap;
  }
  .book__spine-text--author { font-weight: 400; letter-spacing: 2px; }
  .book__cover {
    position: relative; flex: 1; height: 100%; overflow: hidden;
    background: linear-gradient(180deg, #f1f1f2 0%, #d3d4d7 30%, #a7a9ae 60%, #7f838b 100%);
  }
  .book__author {
    position: absolute; left: 0; top: 22px; width: 100%; text-align: center;
    font-family: "Lexend", sans-serif; font-weight: 400; font-size: 12px; letter-spacing: 3px; color: var(--ink);
  }
  .book__photo {
    position: absolute; left: 10px; top: 48px; width: 209px; height: 300px;
    background: radial-gradient(ellipse at 52% 30%, #8b7466 0%, #5b5f6b 35%, #3d4a63 70%, rgba(61,74,99,.4) 100%);
  }
  .book__title { position: absolute; left: 0; top: 200px; width: 100%; font-family: "Anton", sans-serif; line-height: 1; }
  .book__title-word { position: absolute; padding: 2px 5px 3px; white-space: nowrap; }
  .book__title-why { left: 20px; top: 0; font-size: 28px; color: var(--white); background: rgba(70,72,80,.72); }
  .book__title-main { left: 14px; top: 34px; font-size: 40px; color: var(--cover-rose); background: rgba(236,236,238,.88); letter-spacing: .5px; }
  .book__title-end { left: 128px; top: 84px; font-size: 28px; color: var(--white); background: rgba(45,47,55,.82); }
  .book__tagline {
    position: absolute; left: -6px; bottom: 6px; width: 250px; height: 24px; background: #f4f4f5;
    transform: rotate(-4deg); transform-origin: left bottom;
    font-family: "Lexend", sans-serif; font-size: 8.5px; font-weight: 500; color: var(--ink);
    display: flex; align-items: center; justify-content: center; white-space: nowrap;
  }
  .book__tagline b { font-weight: 700; margin: 0 2px; }

  /* Event details */
  .fair-name {
    position: absolute; left: 430px; top: 434px; width: 420px; text-align: center;
    font-family: "Lexend", sans-serif; font-weight: 600; font-size: 14px; color: var(--gold);
  }
  .dates { position: absolute; left: 461px; top: 455px; color: var(--white); font-family: "Anton", sans-serif; line-height: 1; }
  .dates__days { position: absolute; left: 0; top: 0; font-size: 134px; white-space: nowrap; letter-spacing: 2px; }
  .dates__month { position: absolute; left: 199px; top: 4px; font-size: 64px; }
  .dates__year { position: absolute; left: 197px; top: 76px; font-size: 46px; }

  .venue-logo {
    position: absolute; left: 384px; top: 640px; display: flex; align-items: center; gap: 7px;
    font-family: "Lexend", sans-serif; font-weight: 700; font-size: 22px; color: var(--gold);
  }
  .venue-logo__mark { width: 14px; height: 14px; background: var(--gold); }
  .venue-divider { position: absolute; left: 537px; top: 621px; width: 2px; height: 63px; background: var(--text-blue); }
  .venue { position: absolute; left: 551px; top: 633px; font-family: "Lexend", sans-serif; font-style: normal; color: var(--text-blue); }
  .venue__name { font-size: 18px; font-weight: 700; }
  .venue__address { font-size: 13px; font-weight: 600; margin-top: 3px; }

  .tickets {
    position: absolute; left: 0; top: 743px; width: 873px; text-align: center;
    font-family: "Lexend", sans-serif; font-weight: 600; font-size: 15px; color: var(--text-blue);
    letter-spacing: 8.5px;
  }
</style>
</head>
<body>
<main class="canvas">
  <section class="panel">
    <h1 class="headline">
      <span class="headline__big headline__book">BOOK</span>
      <span class="headline__big headline__launch">LAUNCH</span>
      <span class="headline__event">EVENT</span>
    </h1>

    <div class="author-photo" role="img" aria-label="Portrait photo of author Dr Tarek Bismil"></div>
    <p class="author-name">
      <span class="author-name__line author-name__first">Dr. Tarek</span>
      <span class="author-name__line author-name__last">Bismil</span>
    </p>

    <div class="date-band"></div>

    <div class="book">
      <div class="book__spine">
        <span class="book__spine-text">WHY COMFORT STALLS</span>
        <span class="book__spine-text book__spine-text--author">TAREK BISMIL</span>
      </div>
      <div class="book__cover">
        <div class="book__photo" role="img" aria-label="Photo of the author in a suit on the book cover"></div>
        <p class="book__author">TAREK BISMIL</p>
        <div class="book__title">
          <span class="book__title-word book__title-why">WHY</span>
          <span class="book__title-word book__title-main">COMFORT</span>
          <span class="book__title-word book__title-end">STALLS</span>
        </div>
        <p class="book__tagline"><b>SHAPE</b> Your Path With A Fearless New <b>PLAN</b></p>
      </div>
    </div>

    <p class="fair-name">Quillmark Reading Fair and Showcase 2022</p>
    <div class="dates">
      <span class="dates__days">7-8</span>
      <span class="dates__month">Oct</span>
      <span class="dates__year">2022</span>
    </div>

    <div class="venue-logo"><span class="venue-logo__mark"></span>QUILLMARK</div>
    <div class="venue-divider"></div>
    <address class="venue">
      <p class="venue__name">Melbourne Larkvale Centre</p>
      <p class="venue__address">14 Corrigal St, Southbank Melbourne</p>
    </address>

    <p class="tickets">registration and ticketing | penfairhall.com.au</p>
  </section>
</main>
</body>
</html>
```